Brochure Design Project - Brelwick Motors Auto Repair Centre

We require a high quality brochure (A3 folded to A4) for us to send to local businesses to try and get more sales. We would like to keep our current colour scheme from our flyers. We are garagemark approved so we require this logo to be included in the design. The font used on our flyer is QuickLinesRG available from fontvault-example.com
This is a brief of the information we require on our brochure (the feedback from our current customers still to be received but it will be limited to 1 line each) :
Introduction to Brelwick Motors
Based in Cumbernauld, Brelwick Motors are a family run Auto service centre and believe in giving helpful, friendly expert advice in plain English. We have a wealth of experience in a wide range of vehicles and we invest heavily in equipment to ensure our work is completed to the highest possible quality standards.
It is our aim to deliver a quality service at competitive rates for our customers. We have just expanded by investing in a new 4000 sq/ft workshop to help support our ever expanding customer base.
Why are we the best choice for your business?
Choosing a garage for your business can be a tough decision. Who do you choose and who do you trust? Cost will of course be high on your list, so why take your car to a main dealer and pay main dealer prices?
• Brelwick Motors Cumbernauld can carry out servicing and repairs to main dealer standards without the high prices. We can also maintain your vehicles warranty by using genuine manufacturer's parts.
• Communication is key – we never leave you wondering when your vehicle is going to be returned. 98% of vehicles we maintain are returned the same day.
• We never carry out any work to a vehicle without prior agreement – so no unexpected bills. You always get a fully itemised VAT invoice.
• We can arrange payment terms that are suitable to both businesses.
• We have flexibility with our working hours to ensure your fleet stays on the road no matter how big or small.
• We also pride ourselves on providing a professional and efficient service, your vehicle will be looked after as if it was our own pride and joy.
How can we guarantee quality?
Garage mark is the Trading Standards code of practice for garages. We are the only independent garage in Cumbernauld to achieve this standard. We are audited to ensure we comply with the code at all times and we must follow a strict complaints procedure should the need arise.
All parts fitted are covered by a 3 month or 6000 mile warranty. *Does not include wear and tear
What services can we offer your business?
MOT Testing
Vehicle Servicing
Budget & Performance Tyres
Mechanical Repairs
Exhausts, DPF filters & CAT’s
Brake repair specialist
Same day Clutch repairs
Gearboxes
Starter motors
Alternators
Wheel Alignment
MOT Welding
Replacement Batteries
ECU Fault Diagnostics & Service resets
Collection and drop off services
We are comprehensively insured to drive all of our customers’ vehicles so we can collect vehicles at a time that suits you and deliver them back with minimal impact to your business. The only time we will ever drive your vehicles is during transportation or testing.
Our current business customers – testimonials
Pettigrew Roofing
Crest Fitting
Hollowbys
Ruvan Loader training
Sample price list
£74.17 for car service/small vans
£91.67 for commercials up to 3500kgs (class IV)
Mot’s £35 for cars and vans (class IV)
Tyre sample prices – Korvath Hatch £36.95, Delmare Van £32.45, Korvath Cargo £41.55.
Labour rate of £35.00ph
All prices exclude VAT at applicable rate, unless stated otherwise and are correct at time of printing. Subject to change without prior notice. No VAT on MOT's
Contact Us
Brelwick Motors can be contacted to discuss your individual requirement by -
Phone: 01236 482915
Email: sales@brelwick-example.co.uk
Mon – Fri 8.00am – 5.30pm
Sat – 8.00am – 4.00pm
Target Market(s)
local businesses
Industry/Entity Type
Garage
Requirements
Must have
- garagemark logo
brelwick motors logo

```html
<!DOCTYPE html>
<html lang="en">
<head>
<meta charset="utf-8">
<title>Brelwick Motors – Business Brochure</title>
<link href="https://fonts.googleapis.com/css2?family=Orbitron:wght@500;700&family=Open+Sans:wght@300;400;700&display=swap" rel="stylesheet">
<style>
  :root{
    --paper:#ffffff;
    --ink:#4a4d52;
    --blue:#1f73c9;
    --band:#2f343c;
    --band-line:#6b717a;
    --yellow:#f3e21a;
    --white:#ffffff;
    --photo-dark:#1d232b;
    --photo-mid:#5c6673;
    --photo-light:#aab3bd;
  }
  *{box-sizing:border-box;margin:0;padding:0}
  html,body{width:1200px;height:848px;overflow:hidden;background:var(--paper)}
  body{position:relative;font-family:"Open Sans",Arial,sans-serif;font-weight:300;color:var(--ink);font-size:8.6px;line-height:12.6px}
  .heading{font-family:"Orbitron",Arial,sans-serif;font-weight:700;color:var(--blue);font-size:9.8px;letter-spacing:.06em;text-transform:uppercase;line-height:12px}
  .block{position:absolute}

  /* intro column */
  .intro{left:36px;top:290px;width:216px}
  .intro .heading{margin-bottom:12px}
  .intro p{margin-bottom:12.6px}
  .pillars{left:50px;top:470px;list-style:none}
  .pillars li{font-family:"Orbitron",Arial,sans-serif;font-weight:700;color:var(--blue);font-size:9.6px;letter-spacing:.06em;text-transform:uppercase;line-height:12px;margin-bottom:12px}

  /* reasons column */
  .reasons{left:277px;top:35px;width:284px}
  .reasons .heading{margin-bottom:11px}
  .reasons > p{margin-bottom:13px}
  .reasons ul{list-style:none}
  .reasons li{position:relative;padding-left:14px;margin-bottom:12.6px}
  .reasons li::before{content:"";position:absolute;left:14px;top:3px;width:7px;height:7px;border-radius:50%;background:var(--blue)}
  .reasons li span{display:block;text-indent:14px}
  .quality{left:277px;top:398px;width:284px}
  .quality .heading{margin-bottom:11px}
  .quality p{margin-bottom:12.6px}

  /* photos */
  .photo{position:absolute;left:636px;width:286px;height:166px}
  .photo-laptop{top:36px;background:linear-gradient(135deg,var(--photo-light),var(--photo-mid) 45%,var(--photo-dark))}
  .photo-wheel{top:206px;background:linear-gradient(160deg,var(--photo-light),#7d8691 50%,var(--photo-dark))}
  .photo-battery{top:377px;background:linear-gradient(120deg,var(--photo-dark),#3e4a5a 50%,var(--photo-mid))}

  /* services column */
  .services{left:950px;top:35px;width:222px}
  .services .heading{margin-bottom:11px}
  .services ul{list-style:none}
  .services li{position:relative;padding-left:27px;height:24.2px}
  .services li::before{content:"";position:absolute;left:14px;top:3px;width:7px;height:7px;border-radius:50%;background:var(--blue)}
  .collection{left:950px;top:422px;width:222px}
  .collection .heading{margin-bottom:11px}

  /* dark band */
  .band{position:absolute;left:0;top:548px;width:1200px;height:300px}
  .band svg{position:absolute;left:0;top:0}
  .band-body{position:absolute;left:0;top:8px;width:1200px;height:292px;background:var(--band)}

  .reviews-title{left:41px;top:589px;color:var(--yellow)}
  .review{position:absolute;top:647px;width:128px;color:var(--white);font-size:8.6px;line-height:11.8px}
  .review .open{position:absolute;left:-2px;top:-6px;font-family:"Open Sans",Arial,sans-serif;font-weight:700;font-size:30px;line-height:1;color:var(--yellow)}
  .review p{text-indent:20px}
  .review .by{display:block;text-align:right;margin-top:14px;padding-right:6px;font-style:normal}
  .review .close{position:absolute;right:2px;bottom:-34px;font-family:"Open Sans",Arial,sans-serif;font-weight:700;font-size:30px;line-height:1;color:var(--yellow)}

  .prices{left:636px;width:286px;border-collapse:collapse;color:var(--white);font-size:10px;line-height:12px}
  .prices caption{background:var(--yellow);color:var(--band);text-align:left;font-family:"Orbitron",Arial,sans-serif;font-weight:700;letter-spacing:.05em;text-transform:uppercase;padding:4px 5px;width:286px;caption-side:top}
  .prices td{border-bottom:1px solid var(--band-line);padding:5px 5px;height:24px}
  .prices td.amount{border-left:1px solid var(--band-line);width:78px}
  .sample-prices{top:583px}
  .sample-prices caption{font-size:9.4px}
  .tyre-prices{top:698px}
  .tyre-prices caption{font-size:11.5px}

  .brand{position:absolute;left:950px;top:676px;display:flex;align-items:center;gap:10px}
  .brand-mark{width:36px;height:36px;border-radius:50%;background:var(--yellow)}
  .brand-name{font-family:"Orbitron",Arial,sans-serif;font-weight:700;color:var(--white);font-size:18px;letter-spacing:.04em;line-height:1.1;text-transform:uppercase}
  .small-print{position:absolute;left:950px;top:764px;width:222px;color:var(--white);font-size:8.6px;line-height:11.6px}
</style>
</head>
<body>

  <section class="block intro">
    <h2 class="heading">Brelwick Motors</h2>
    <p>Based in Cumbernauld, Brelwick Motors are a family run Auto service centre and believe in giving helpful, friendly expert advice in plain English. We have a wealth of experience in a wide range of vehicles and we invest heavily in equipment to ensure our work is completed to the highest possible quality standards.</p>
    <p>It is our aim to deliver a quality service at competitive rates for our customers. We have just expanded by investing in a new 4000 sq/ft workshop to help support our ever expanding customer base.</p>
  </section>
  <ul class="block pillars">
    <li>Finest customer service</li>
    <li>Competitive prices</li>
    <li>Quality workmanship</li>
  </ul>

  <section class="block reasons">
    <h2 class="heading">Why are we the best choice<br>for your business?</h2>
    <p>Choosing a garage for your business can be a tough decision. Who do you choose and who do you trust? Cost will of course be high on your list, so why take your car to a main dealer and pay main dealer prices?</p>
    <ul>
      <li><span>Brelwick Motors Cumbernauld can carry out servicing and repairs to main dealer standards without the high prices. We can also maintain your vehicles warranty by using genuine manufacturer's parts.</span></li>
      <li><span>Communication is key – we never leave you wondering when your vehicle is going to be returned. 98% of vehicles we maintain are returned the same day.</span></li>
      <li><span>We never carry out any work to a vehicle without prior agreement – so no unexpected bills. You always get a fully itemised VAT invoice.</span></li>
      <li><span>We can arrange payment terms suitable to both businesses.</span></li>
      <li><span>We have flexibility with our working hours to ensure your fleet stays on the road no matter how big or small.</span></li>
      <li><span>We also pride ourselves on providing a professional and efficient service, your vehicle will be looked after as if it was our own pride and joy.</span></li>
    </ul>
  </section>
  <section class="block quality">
    <h2 class="heading">How can we guarantee quality?</h2>
    <p>Garage mark is the Trading Standards code of practice for garages. We are the only independent garage in Cumbernauld to achieve this standard. We are audited to ensure we comply with the code at all times and we must follow a strict complaints procedure should the need arise.</p>
    <p>All parts fitted are covered by a 3 month or 6000 mile warranty.*</p>
    <p>*Does not include wear and tear</p>
  </section>

  <div class="photo photo-laptop" role="img" aria-label="Photo of a mechanic running engine diagnostics on a laptop"></div>
  <div class="photo photo-wheel" role="img" aria-label="Photo of a wheel mounted on a balancing machine in a workshop"></div>
  <div class="photo photo-battery" role="img" aria-label="Photo of hands fitting a replacement car battery"></div>

  <section class="block services">
    <h2 class="heading">What services can we offer<br>your business?</h2>
    <ul>
      <li>MOT Testing</li>
      <li>Vehicle Servicing</li>
      <li>Budget &amp; Performance Tyres</li>
      <li>Mechanical Repairs</li>
      <li>Exhausts, DPF filters &amp; CAT's</li>
      <li>Brake repair specialist</li>
      <li>Same day Clutch repairs</li>
      <li>Gearboxes</li>
      <li>Starter motors</li>
      <li>Alternators</li>
      <li>Wheel Alignment</li>
      <li>MOT Welding</li>
      <li>Replacement Batteries</li>
      <li>ECU Fault Diagnostics &amp; Service resets</li>
    </ul>
  </section>
  <section class="block collection">
    <h2 class="heading">Collection<br>and drop off services</h2>
    <p>We are comprehensively insured to drive all of our customers' vehicles so we can collect vehicles at a time that suits you and deliver them back with minimal impact to your business. The only time we will ever drive your vehicles is during transportation or testing.</p>
  </section>

  <div class="band">
    <svg width="1200" height="10" aria-hidden="true">
      <defs>
        <pattern id="teeth" width="14.4" height="10" patternUnits="userSpaceOnUse">
          <polygon points="2,10 4,1 10,1 12,10" fill="#2f343c"/>
        </pattern>
      </defs>
      <rect width="1200" height="10" fill="url(#teeth)"/>
    </svg>
    <div class="band-body"></div>
  </div>

  <h2 class="block heading reviews-title">What our customers say about us</h2>

  <blockquote class="review" style="left:41px">
    <span class="open">"</span>
    <p>Lorem ipsum dolor sit amet, consetetur sadipscing elitr, sed diam nonumy eirmod tempor invidunt ut labore et dolore magna aliquyam erat, sed diam voluptua.</p>
    <cite class="by">- Pettigrew Roofing</cite>
    <span class="close">"</span>
  </blockquote>
  <blockquote class="review" style="left:175px">
    <span class="open">"</span>
    <p>Lorem ipsum dolor sit amet, consetetur sadipscing elitr, sed diam nonumy eirmod tempor invidunt ut labore et dolore magna aliquyam erat, sed diam voluptua.</p>
    <cite class="by">- Crest Fitting</cite>
    <span class="close">"</span>
  </blockquote>
  <blockquote class="review" style="left:310px">
    <span class="open">"</span>
    <p>Lorem ipsum dolor sit amet, consetetur sadipscing elitr, sed diam nonumy eirmod tempor invidunt ut labore et dolore magna aliquyam erat, sed diam voluptua.</p>
    <cite class="by">- Hollowbys</cite>
    <span class="close">"</span>
  </blockquote>
  <blockquote class="review" style="left:444px">
    <span class="open">"</span>
    <p>Lorem ipsum dolor sit amet, consetetur sadipscing elitr, sed diam nonumy eirmod tempor invidunt ut labore et dolore magna aliquyam erat, sed diam voluptua.</p>
    <cite class="by">- Ruvan Loader Training</cite>
    <span class="close">"</span>
  </blockquote>

  <table class="block prices sample-prices">
    <caption>Sample price list</caption>
    <tr><td>Car/Small vans Service</td><td class="amount">£ 74.17</td></tr>
    <tr><td>Commercials up to 3500kgs (class IV)</td><td class="amount">£91.67</td></tr>
    <tr><td>Mot's for cars and vans (class IV)</td><td class="amount">£ 35.00</td></tr>
  </table>

  <table class="block prices tyre-prices">
    <caption>Tyre sample prices</caption>
    <tr><td>Korvath Hatch</td><td class="amount">£ 36.95</td></tr>
    <tr><td>Delmare Van</td><td class="amount">£ 32.45</td></tr>
    <tr><td>Korvath Cargo £41.55</td><td class="amount">£ 41.55</td></tr>
    <tr><td>Labour rate</td><td class="amount">£ 35.00ph</td></tr>
  </table>

  <div class="brand">
    <span class="brand-mark"></span>
    <span class="brand-name">Brelwick<br>Motors</span>
  </div>
  <p class="small-print">All prices exclude VAT at applicable rate, unless stated otherwise and are correct at time of printing. Subject to change without prior notice.<br>No VAT on MOT's</p>

</body>
</html>
```